Quarry Lane Co. needs Business Cards

For this project, we need business cards (currently have also put a call out for a logo). We are a start-up called Quarry Lane Co. This is our second company (our first one was called Brightwickery). Traditionally we have been providing market research services across different sectors, primarily financial services and the pharmaceutical industry. However, we now want to go beyond market research to offer more (Etc.)... strategic consulting and big data knowledge management. We want our brand to be approachable, creative, fun but professional.

Target Market(s)

The target audience is a business professional - we are B2B (business to business) and do not sell our services to individuals. The brands we work with are major brands across industries, but primarily automotive, financial and pharmaceutical.

Industry/Entity Type

Market Research

Font styles to use
Serif
Sans Serif
Other font styles liked:
• Calibri

Requirements
Must have
• Be clean, simple, modern
Show our address and phone number and email address and website URL
We do not need to have titles showing.

```html
<!DOCTYPE html>
<html lang="en">
<head>
<meta charset="utf-8">
<title>Quarry Lane Co. — Business Card</title>
<link rel="stylesheet" href="https://fonts.googleapis.com/css2?family=Michroma&display=swap">
<style>
  :root {
    --page-bg: #e4e5e8;
    --card-white: #ffffff;
    --card-shade: #eceded;
    --brand-blue: #0c5198;
    --brand-red: #d3163a;
    --ink: #2b2b2b;
    --ink-soft: #3a3a3a;
  }
  * { margin: 0; padding: 0; box-sizing: border-box; }
  html, body {
    width: 1200px;
    height: 900px;
    overflow: hidden;
    background: var(--page-bg);
    font-family: "Michroma", sans-serif;
  }
  .card {
    position: absolute;
    left: 110px;
    top: 170px;
    width: 980px;
    height: 560px;
    border-radius: 56px;
    overflow: hidden;
    background: radial-gradient(ellipse at 45% 40%, var(--card-white) 0%, var(--card-white) 40%, var(--card-shade) 100%);
    box-shadow: 0 10px 30px rgba(0,0,0,0.12);
  }
  .card__swoosh {
    position: absolute;
    inset: 0;
    width: 100%;
    height: 100%;
  }
  .swoosh--blue { fill: var(--brand-blue); }
  .swoosh--red { fill: var(--brand-red); }

  .wordmark {
    position: absolute;
    left: 62px;
    top: 200px;
    font-size: 40px;
    color: var(--brand-blue);
    letter-spacing: -0.5px;
    white-space: nowrap;
  }

  .holder {
    position: absolute;
    right: 70px;
    top: 50px;
    text-align: right;
  }
  .holder__name {
    font-size: 21px;
    color: var(--brand-red);
    letter-spacing: 1px;
  }
  .holder__title {
    font-size: 13px;
    color: var(--ink);
    letter-spacing: 1px;
    margin-top: 4px;
  }

  .contact {
    position: absolute;
    right: 46px;
    top: 136px;
    list-style: none;
    text-align: right;
  }
  .contact__item {
    display: flex;
    justify-content: flex-end;
    align-items: center;
    gap: 10px;
    font-size: 13.5px;
    color: var(--ink);
    height: 28px;
  }
  .contact__icon {
    width: 18px;
    height: 18px;
    fill: var(--brand-red);
    flex: none;
  }

  .address {
    position: absolute;
    left: 62px;
    top: 362px;
    font-size: 18px;
    font-style: normal;
    line-height: 30px;
    color: var(--ink-soft);
  }
</style>
</head>
<body>
  <article class="card">
    <svg class="card__swoosh" viewBox="0 0 980 560" preserveAspectRatio="none" aria-hidden="true">
      <path class="swoosh--blue" d="M0,478 C300,476 560,444 740,402 C860,374 940,352 980,340 L980,560 L0,560 Z"/>
      <path class="swoosh--red" d="M230,452 C470,440 700,390 860,340 C920,320 960,305 980,298 L980,322 C940,334 880,352 790,374 C600,424 420,450 230,452 Z"/>
    </svg>

    <div class="wordmark">QUARRY LANE CO.</div>

    <header class="holder">
      <div class="holder__name">DANA HOLLOWAY</div>
      <div class="holder__title">PRESIDENT</div>
    </header>

    <ul class="contact">
      <li class="contact__item">014 287 5530
        <svg class="contact__icon" viewBox="0 0 24 24"><path d="M6.6 10.8c1.4 2.8 3.8 5.1 6.6 6.6l2.2-2.2c.3-.3.7-.4 1-.2 1.1.4 2.3.6 3.6.6.6 0 1 .4 1 1V20c0 .6-.4 1-1 1C10.6 21 3 13.4 3 4c0-.6.4-1 1-1h3.5c.6 0 1 .4 1 1 0 1.3.2 2.5.6 3.6.1.3 0 .7-.2 1L6.6 10.8z"/></svg>
      </li>
      <li class="contact__item">014 287 5531
        <svg class="contact__icon" viewBox="0 0 24 24"><path d="M7 2h10a2 2 0 0 1 2 2v16a2 2 0 0 1-2 2H7a2 2 0 0 1-2-2V4a2 2 0 0 1 2-2zm0 3v13h10V5H7z"/></svg>
      </li>
      <li class="contact__item">014 287 5532
        <svg class="contact__icon" viewBox="0 0 24 24"><path d="M7 3h8l3 3v5H7V3zm-2 9h14a2 2 0 0 1 2 2v6a1 1 0 0 1-1 1H4a1 1 0 0 1-1-1v-6a2 2 0 0 1 2-2zm2 3v2h3v-2H7zm5 0v2h2v-2h-2zm4 0v2h2v-2h-2z"/></svg>
      </li>
      <li class="contact__item">hello@quarrylane.co
        <svg class="contact__icon" viewBox="0 0 24 24"><path d="M3 5h18a1 1 0 0 1 1 1v12a1 1 0 0 1-1 1H3a1 1 0 0 1-1-1V6a1 1 0 0 1 1-1zm1 2.3V17h16V7.3l-8 5.4-8-5.4zM5.6 7 12 11.3 18.4 7H5.6z"/></svg>
      </li>
      <li class="contact__item">www.quarrylane.co
        <svg class="contact__icon" viewBox="0 0 24 24"><path d="M12 2a10 10 0 1 1 0 20 10 10 0 0 1 0-20zm-1.2 2.1A8 8 0 0 0 4.1 11h3.4c.1-2.6.9-5 2.1-6.9zm2.4 0c1.2 1.9 2 4.3 2.1 6.9h3.4a8 8 0 0 0-5.5-6.9zM9.5 11h5c-.1-2.5-1-4.7-2.5-6.4-1.5 1.7-2.4 3.9-2.5 6.4zm-5.4 2a8 8 0 0 0 6.7 6.9c-1.2-1.9-2-4.3-2.1-6.9H4.1zm5.4 0c.1 2.5 1 4.7 2.5 6.4 1.5-1.7 2.4-3.9 2.5-6.4h-5zm7 0c-.1 2.6-.9 5-2.1 6.9a8 8 0 0 0 5.5-6.9h-3.4z"/></svg>
      </li>
    </ul>

    <address class="address">
      41.9th floor,Arden<br>
      Millbrook Road QLC
    </address>
  </article>
</body>
</html>
```